Business Card Design Project

We need business cards for the new company Market Helix based in Abu Dhabi, UAE, which provides IT retail solutions to businesses
Design should be done as a template, so we can add people when needed.
Please see attached details.
The brief is about 2 companies from our group. We need a business card only for Market Helix
Industry/Entity Type
Retail
Look and feel
Each slider illustrates characteristics of the customer's brand and the style your logo design should communicate.

```html
<!DOCTYPE html>
<html lang="en">
<head>
<meta charset="utf-8">
<title>Market Helix – Business Card</title>
<link href="https://fonts.googleapis.com/css2?family=Noto+Serif:wght@400;700&family=Noto+Naskh+Arabic:wght@400;700&family=Roboto:wght@500;900&display=swap" rel="stylesheet">
<style>
  :root {
    --purple: #7b1fa2;
    --purple-deep: #5e1380;
    --purple-light: #9a3cc0;
    --gold: #d4a81c;
    --paper: #fbfbfb;
    --ink: #222222;
    --muted: #555555;
    --backdrop: #e6e6e6;
  }
  * { margin: 0; padding: 0; box-sizing: border-box; }
  html, body { width: 1200px; height: 900px; overflow: hidden; }
  body {
    background: var(--backdrop);
    font-family: "Noto Serif", serif;
    position: relative;
  }
  .card {
    position: absolute;
    width: 560px;
    height: 320px;
    border-radius: 10px;
    overflow: hidden;
    box-shadow: 0 8px 24px rgba(0,0,0,0.18);
  }
  .card-front {
    left: 90px;
    top: 110px;
    background: var(--paper);
  }
  .front-band {
    position: absolute;
    left: 0; right: 0; bottom: 0;
    height: 320px;
  }
  .brand {
    position: absolute;
    left: 40px;
    top: 150px;
    display: flex;
    align-items: center;
    gap: 10px;
  }
  .brand-dot {
    width: 18px; height: 18px;
    border-radius: 50%;
    background: var(--gold);
  }
  .brand-name {
    font-family: "Roboto", sans-serif;
    font-weight: 900;
    font-size: 32px;
    color: var(--purple);
    letter-spacing: 0.5px;
    white-space: nowrap;
  }
  .front-web {
    position: absolute;
    left: 40px;
    top: 210px;
    font-weight: 700;
    font-size: 17px;
    color: var(--purple);
    letter-spacing: 1px;
  }
  .details {
    position: absolute;
    left: 300px;
    top: 32px;
    width: 240px;
  }
  .person-name {
    font-weight: 700;
    font-size: 17px;
    color: var(--ink);
  }
  .arabic {
    font-family: "Noto Naskh Arabic", serif;
    direction: rtl;
    text-align: left;
    unicode-bidi: plaintext;
  }
  .person-name-ar { font-size: 14px; color: var(--ink); margin-top: 2px; }
  .person-title {
    font-size: 12px;
    color: var(--purple);
    margin-top: 8px;
  }
  .person-title-ar { font-size: 11px; color: var(--purple); }
  .address {
    font-size: 10px;
    color: var(--muted);
    margin-top: 10px;
  }
  .address-ar { font-size: 10px; color: var(--muted); }
  .contact-list { list-style: none; margin-top: 8px; }
  .contact-item {
    display: flex;
    align-items: center;
    gap: 7px;
    font-size: 10px;
    color: var(--muted);
    line-height: 18px;
  }
  .contact-icon {
    width: 13px; height: 13px;
    border-radius: 50%;
    border: 1px solid var(--purple-light);
    color: var(--purple);
    font-family: "Roboto", sans-serif;
    font-size: 7px;
    display: flex; align-items: center; justify-content: center;
  }
  .card-back {
    left: 550px;
    top: 470px;
    background: radial-gradient(circle at 35% 40%, var(--purple-light) 0%, var(--purple) 55%, var(--purple-deep) 100%);
  }
  .back-brand {
    position: absolute;
    left: 0; right: 0;
    top: 110px;
    display: flex;
    justify-content: center;
    align-items: center;
    gap: 12px;
  }
  .back-brand .brand-name { color: #ffffff; font-size: 42px; }
  .back-web {
    position: absolute;
    left: 0; right: 0;
    top: 190px;
    text-align: center;
    font-weight: 700;
    font-size: 17px;
    color: var(--gold);
    letter-spacing: 2px;
  }
</style>
</head>
<body>
  <section class="card card-front" aria-label="Business card front">
    <svg class="front-band" viewBox="0 0 560 320" preserveAspectRatio="none" aria-hidden="true">
      <path d="M0 292 Q280 300 560 262 L560 320 L0 320 Z" fill="var(--purple)"/>
      <path d="M0 290 Q280 298 560 260" stroke="var(--gold)" stroke-width="3" fill="none"/>
    </svg>
    <div class="brand">
      <span class="brand-dot"></span>
      <span class="brand-name">Market Helix</span>
    </div>
    <div class="front-web">www.helixretail.ae</div>
    <div class="details">
      <p class="person-name">Karim Haddad Saleh</p>
      <p class="person-name-ar arabic">كريم حداد</p>
      <p class="person-title">Retail Solutions Manager</p>
      <p class="person-title-ar arabic">مدير حلول التجزئة</p>
      <p class="address">PO Box 10250, Abu Dhabi, UAE</p>
      <p class="address-ar arabic">أبوظبي، الإمارات</p>
      <ul class="contact-list">
        <li class="contact-item"><span class="contact-icon">T</span>971 2 555 0140 – Ext: 310</li>
        <li class="contact-item"><span class="contact-icon">F</span>+971 2 555 0148</li>
        <li class="contact-item"><span class="contact-icon">M</span>+971 50 555 0192</li>
        <li class="contact-item"><span class="contact-icon">E</span>k.saleh@helixretail.ae</li>
      </ul>
    </div>
  </section>

  <section class="card card-back" aria-label="Business card back">
    <div class="back-brand">
      <span class="brand-dot"></span>
      <span class="brand-name">Market Helix</span>
    </div>
    <div class="back-web">www.helixretail.ae</div>
  </section>
</body>
</html>
```